BrightHarbor, LLC
BrightHarbor
Creative Brief
Professional
Joan Ferris
Executive & Clinical Director
7183 Marbrook Avenue St. Louis, MO 63902
jferris@brightharborcare.example
www.brightharborcare.example
Card # 2 Nora Whitfield Marketing & Operations Director 7183 Marbrook Avenue St. Louis, MO 63902 Office Tel: 314-555-0172 Cell Tel: 314-555-0198 nwhitfield42@brightharborcare.example www.brightharborcare.example
WE APPRECIATE REFERRALS

```html
<!DOCTYPE html>
<html lang="en">
<head>
<meta charset="utf-8">
<title>BrightHarbor, LLC — Business Card</title>
<link href="https://fonts.googleapis.com/css2?family=Didact+Gothic&display=swap" rel="stylesheet">
<style>
  :root {
    --page: #ecebe8;
    --card: #ffffff;
    --ink: #4a4a4c;
    --grey: #8c8c8e;
    --orange: #f39a2b;
    --faint: #f7f2ea;
  }
  * { margin: 0; padding: 0; box-sizing: border-box; }
  html, body { width: 1200px; height: 904px; overflow: hidden; }
  body {
    background: var(--page);
    font-family: "Didact Gothic", "Century Gothic", sans-serif;
    color: var(--ink);
    position: relative;
  }
  .card {
    position: absolute;
    width: 700px;
    height: 400px;
    background: var(--card);
    border-radius: 22px;
    box-shadow: 0 6px 18px rgba(0,0,0,0.12);
    overflow: hidden;
  }
  .card--back { left: 80px; top: 52px; }
  .card--front { left: 420px; top: 476px; }

  .brand-mark {
    display: flex;
    align-items: center;
    gap: 10px;
  }
  .brand-mark__dot {
    width: 22px; height: 22px;
    border-radius: 50%;
    background: var(--orange);
  }
  .brand-mark__name {
    color: var(--grey);
    font-size: 30px;
  }
  .card--back .brand-mark {
    position: absolute;
    left: 50%; top: 50%;
    transform: translate(-50%, -50%);
  }

  .watermark-circle {
    position: absolute;
    right: -40px; top: -70px;
    width: 320px; height: 320px;
    border-radius: 50%;
    background: var(--faint);
  }

  .front-brand {
    position: absolute;
    left: 44px; top: 58px;
  }
  .front-brand .brand-mark__name { font-size: 26px; }
  .tagline {
    margin: 4px 0 0 32px;
    font-size: 11px;
    letter-spacing: 1px;
    color: var(--orange);
  }

  .contact {
    position: absolute;
    left: 44px; top: 178px;
    font-size: 15px;
    line-height: 1.3;
  }
  .contact__address { margin-bottom: 10px; }
  .contact__list { list-style: none; }
  .contact__list li {
    display: flex;
    align-items: center;
    gap: 10px;
    height: 22px;
  }
  .contact__list svg { width: 14px; height: 14px; fill: var(--orange); flex: none; }

  .person {
    position: absolute;
    left: 368px; top: 210px;
  }
  .person__name { color: var(--orange); font-size: 21px; }
  .person__title { font-size: 15px; margin-top: 2px; }
</style>
</head>
<body>

<section class="card card--back" aria-label="Card back">
  <div class="brand-mark">
    <span class="brand-mark__dot"></span>
    <span class="brand-mark__name">BrightHarbor</span>
  </div>
</section>

<section class="card card--front" aria-label="Card front">
  <div class="watermark-circle"></div>

  <div class="front-brand">
    <div class="brand-mark">
      <span class="brand-mark__dot"></span>
      <span class="brand-mark__name">BrightHarbor, LLC</span>
    </div>
    <p class="tagline">Compassionate Senior Living</p>
  </div>

  <div class="contact">
    <p class="contact__address">7183 Marbrook Avenue<br>St. Louis, MO 63902</p>
    <ul class="contact__list">
      <li><svg viewBox="0 0 16 16"><path d="M3 1h3l1.5 4-2 1.2a9 9 0 0 0 4.3 4.3L11 8.5l4 1.5v3a2 2 0 0 1-2 2A12 12 0 0 1 1 3a2 2 0 0 1 2-2z"/></svg>314-555-0172</li>
      <li><svg viewBox="0 0 16 16"><path d="M4 0h8a1 1 0 0 1 1 1v14a1 1 0 0 1-1 1H4a1 1 0 0 1-1-1V1a1 1 0 0 1 1-1zm1 2v10h6V2zm3 11a1 1 0 1 0 0 2 1 1 0 0 0 0-2z"/></svg>314-555-0134</li>
      <li><svg viewBox="0 0 16 16"><path d="M4 1h7v4H4zM2 6h12a1 1 0 0 1 1 1v6H1V7a1 1 0 0 1 1-1zm3 5h6v4H5z"/></svg>314-555-0156</li>
      <li><svg viewBox="0 0 16 16"><path d="M1 3h14v10H1zm1.5 1.5v.3L8 9l5.5-4.2v-.3z"/></svg>jferris@brightharborcare.example</li>
      <li><svg viewBox="0 0 16 16"><circle cx="8" cy="8" r="7"/></svg>www.brightharborcare.example</li>
    </ul>
  </div>

  <div class="person">
    <p class="person__name">Joan Ferris</p>
    <p class="person__title">Executive &amp; Clinical Director</p>
  </div>
</section>

</body>
</html>
```